We need visit card and a letter paper for our website. thx

We have a beauty clinic in Switzerland.
https://wolkenbachtal.ch
We need a visit card.

Requirements
Must have
• see colors on website

```html
<!DOCTYPE html>
<html lang="en">
<head>
<meta charset="utf-8">
<title>Wolkenbachtal – Letterhead</title>
<link rel="stylesheet" href="https://fonts.googleapis.com/css2?family=Arimo:wght@400&family=Poppins:wght@300;400&display=swap">
<style>
  :root {
    --rose: #c2446f;
    --rose-light: #ebbccb;
    --ink: #3f3f3f;
    --ink-soft: #555555;
    --paper: #ffffff;
    --paper-shade: #f1f2f2;
  }
  * { margin: 0; padding: 0; box-sizing: border-box; }
  html, body { width: 1098px; height: 1200px; overflow: hidden; }
  body { background: var(--paper); }

  .letterhead {
    position: relative;
    width: 1098px;
    height: 1200px;
    background: linear-gradient(135deg, var(--paper) 35%, var(--paper-shade) 100%);
    color: var(--ink);
    font-family: "Arimo", Arial, sans-serif;
  }

  .brand {
    position: absolute;
    left: 80px;
    top: 104px;
    display: flex;
    align-items: center;
    gap: 14px;
  }
  .brand-mark {
    width: 14px;
    height: 14px;
    background: var(--rose);
  }
  .brand-name {
    font-family: "Poppins", Arial, sans-serif;
    font-weight: 400;
    font-size: 28px;
    color: #1c1c1c;
    letter-spacing: 0.2px;
  }

  .contact {
    position: absolute;
    right: 80px;
    top: 78px;
    padding-left: 26px;
    border-left: 1px solid var(--rose);
    font-family: "Poppins", Arial, sans-serif;
    font-weight: 300;
    font-size: 13.5px;
    line-height: 17px;
    color: #333;
    list-style: none;
  }
  .contact li {
    display: flex;
    align-items: flex-start;
    gap: 10px;
    margin-bottom: 2px;
  }
  .contact li:first-child { margin-bottom: 5px; }
  .contact svg { flex: none; width: 12px; height: 12px; margin-top: 2px; fill: var(--rose); }

  .letter {
    position: absolute;
    left: 80px;
    right: 80px;
    top: 318px;
  }
  .salutation {
    font-size: 22px;
    color: var(--ink-soft);
    margin-bottom: 38px;
  }
  .letter p {
    font-size: 13px;
    line-height: 19px;
    color: var(--ink);
    text-align: justify;
    margin-bottom: 18px;
  }
  .closing { margin-top: 36px; font-size: 13px; }
  .signature {
    margin-top: 24px;
    margin-left: -14px;
    width: 180px;
    height: 64px;
    background: linear-gradient(90deg, #ececec, #f6f6f6);
    border-radius: 4px;
  }

  .footer-band {
    position: absolute;
    left: 0;
    bottom: 14px;
    width: 1098px;
    height: 12px;
  }
</style>
</head>
<body>
  <main class="letterhead">
    <header>
      <div class="brand">
        <span class="brand-mark"></span>
        <span class="brand-name">Wolkenbachtal</span>
      </div>

      <ul class="contact">
        <li>
          <svg viewBox="0 0 12 12"><path d="M6 0a4.2 4.2 0 0 0-4.2 4.2C1.8 7.4 6 12 6 12s4.2-4.6 4.2-7.8A4.2 4.2 0 0 0 6 0zm0 5.8a1.6 1.6 0 1 1 0-3.2 1.6 1.6 0 0 1 0 3.2z"/></svg>
          <span>Talweg 24<br>7550 Wolkenbach, Schweiz</span>
        </li>
        <li>
          <svg viewBox="0 0 12 12"><path d="M2.4 0.6l1.9 2.4-1 1.3c.7 1.6 2 2.9 3.6 3.6l1.3-1 2.4 1.9-.9 2.1C5.3 10.8 1.2 6.7.3 1.5z"/></svg>
          <span>+41 (0) 800 20 30 40</span>
        </li>
        <li>
          <svg viewBox="0 0 12 12"><path d="M0 2.5h12v7H0z M0.6 2.9L6 6.7l5.4-3.8" stroke="#fff" stroke-width=".9"/></svg>
          <span>hallo@wolkenbachtal.ch</span>
        </li>
        <li>
          <svg viewBox="0 0 12 12"><circle cx="6" cy="6" r="5.6"/><path d="M.6 6h10.8M6 .4c-2.4 3-2.4 8.2 0 11.2M6 .4c2.4 3 2.4 8.2 0 11.2" stroke="#fff" stroke-width=".8" fill="none"/></svg>
          <span>www.wolkenbachtal.ch</span>
        </li>
      </ul>
    </header>

    <article class="letter">
      <h1 class="salutation" style="font-weight:400">Dear Mr. Keller,</h1>

      <p>Lorem ipsum dolor sit amet, consectetur adipiscing elit. Donec orci purus, luctus vitae dignissim eu, iaculis sed purus. Vivamus faucibus, ipsum nec aliquet viverra, leo mauris condimentum ligula, sit amet sagittis enim ligula quis arcu. Nam egestas tortor id nisi porttitor mattis. In tortor ante, ultricies in suscipit a, tempus non massa. Vivamus et auctor mi. Fusce vel massa nulla. Phasellus nec eros mauris, et scelerisque orci.</p>

      <p>Donec malesuada orci vitae nulla accumsan porta a id massa. Quisque accumsan iaculis magna sit amet fringilla. Maecenas consequat, magna eget tincidunt semper, odio nibh rutrum mi, id feugiat ante nisi eu risus. Vestibulum nunc orci, rhoncus a placerat in, ultricies in mi. Cras mattis varius eros, vel fringilla nisi suscipit eget. Quisque scelerisque sagittis nulla at porttitor.</p>

      <p>Sed id augue vitae urna euismod commodo aliquet a quam. Pellentesque arcu velit, cursus et malesuada ut, consequat et diam. Nullam erat sem, rhoncus id ullamcorper vitae, rhoncus et arcu. In ultricies ultricies nulla, ut rutrum nisi iaculis at. Donec eu magna a metus ornare faucibus. Fusce aliquet faucibus ultricies. Morbi semper, est id tincidunt gravida, sem arcu adipiscing lacus, ac bibendum nulla leo eu purus. Quisque nec diam sed risus consectetur a ccumsan quis quis nibh. Vestibulum id purus lorem.</p>

      <p>It is a long established fact that a reader will be distracted by the readable content of a page when looking at its layout. The point of using Lorem Ipsum is that it has a more-or-less normal distribution of letters, as opposed to using 'Content here, content here', making it look like readable English. Many desktop publishing packages</p>

      <p>ada ut, consequat et diam. Nullam erat sem, rhoncus id ullamcorper vitae, rhoncus et arcu. In ultricies ultricies nulla, ut rutrum nisi iaculis at. Donec eu magna a metus ornare faucibus. Fusce aliquet faucibus ultricies. Morbi semper,</p>

      <div class="closing">Sincerely,</div>
      <div class="signature" role="img" aria-label="Handwritten signature of the clinic's doctor"></div>
    </article>

    <svg class="footer-band" viewBox="0 0 1098 12" preserveAspectRatio="none" aria-hidden="true">
      <polygon points="0,0 950,0 942,12 0,12" fill="var(--rose)"/>
      <polygon points="954,0 1098,0 1098,12 946,12" fill="var(--rose-light)"/>
    </svg>
  </main>
</body>
</html>
```